Dorrish Electric Ltd

Looking for a single page website and Facebook page design. I am an electrical contractor based on Vancouver Island. I do service, custom homes, residential and commercial installations. My company just started out, so I don't have any pictures of installs yet. I have 25 years experience. I would like the colors to be my logo colors black and I have a black Corvan Ridgeback that will be my vehicle which I will have a wrap for.
Updates

I just posted the contest today, not sure why the deadline is the same day.

Went on vacation/holiday

Industry/Entity Type

Electrician

Requirements
Must have
• Services provided, About me section, quote section,
Nice to have
• I am not quite sure yet, I need to see some designs first .

```html
<!DOCTYPE html>
<html lang="en">
<head>
<meta charset="utf-8">
<title>Dorrish Electric Ltd — Cover</title>
<link href="https://fonts.googleapis.com/css2?family=Montserrat:wght@600;700&family=Open+Sans:wght@400;600&display=swap" rel="stylesheet">
<style>
  :root {
    --ink: #0b0b0b;
    --yellow: #f7b90f;
    --white: #ffffff;
    --soft: #e9e9e9;
    --photo-dark: #3a4350;
    --photo-mid: #8f9aa6;
    --photo-light: #d7dde2;
  }
  html, body {
    margin: 0;
    padding: 0;
    overflow: hidden;
    background: var(--ink);
  }
  .cover {
    position: relative;
    width: 1200px;
    height: 444px;
    background: var(--ink);
    overflow: hidden;
    font-family: "Open Sans", sans-serif;
    color: var(--white);
  }
  .cover__art {
    position: absolute;
    inset: 0;
    width: 1200px;
    height: 444px;
  }
  .brand-mark {
    position: absolute;
    left: 150px;
    top: 78px;
    display: flex;
    align-items: center;
    gap: 14px;
  }
  .brand-mark__dot {
    width: 34px;
    height: 34px;
    border-radius: 50%;
    background: var(--yellow);
  }
  .brand-mark__name {
    font-family: "Montserrat", sans-serif;
    font-weight: 700;
    font-size: 44px;
    color: var(--white);
    letter-spacing: 1px;
  }
  .company-name {
    position: absolute;
    left: 74px;
    top: 226px;
    margin: 0;
    font-family: "Montserrat", sans-serif;
    font-weight: 600;
    font-size: 31px;
    letter-spacing: 0.5px;
    white-space: nowrap;
  }
  .company-name__accent { color: var(--yellow); }
  .tagline {
    position: absolute;
    left: 74px;
    top: 280px;
    width: 500px;
    margin: 0;
    font-size: 16.5px;
    line-height: 24px;
    color: var(--soft);
  }
  .join-button {
    position: absolute;
    left: 74px;
    top: 360px;
    width: 78px;
    height: 22px;
    border-radius: 3px;
    background: var(--yellow);
    color: var(--ink);
    font-family: "Montserrat", sans-serif;
    font-weight: 700;
    font-size: 12px;
    line-height: 22px;
    text-align: center;
    letter-spacing: 0.5px;
  }
  .web-address {
    position: absolute;
    left: 74px;
    top: 389px;
    font-size: 13px;
    letter-spacing: 1.4px;
    color: var(--soft);
  }
  .social-row {
    position: absolute;
    left: 338px;
    top: 389px;
    display: flex;
    align-items: center;
    gap: 6px;
    font-size: 13px;
    letter-spacing: 1.4px;
    color: var(--soft);
  }
  .social-row__dot {
    width: 17px;
    height: 17px;
    border-radius: 50%;
    background: var(--yellow);
  }
  .social-row__handle { margin-left: 6px; }
</style>
</head>
<body>
  <main class="cover">
    <svg class="cover__art" viewBox="0 0 1200 444" aria-hidden="false">
      <defs>
        <linearGradient id="panelWork" x1="0" y1="0" x2="1" y2="1">
          <stop offset="0" stop-color="var(--photo-light)"/>
          <stop offset="0.45" stop-color="var(--photo-mid)"/>
          <stop offset="1" stop-color="var(--photo-dark)"/>
        </linearGradient>
      </defs>
      <polygon class="accent-white" points="590,0 738,0 666,180" fill="var(--white)"/>
      <g role="img" aria-label="Electrician's hands fitting breakers and wiring in a distribution panel">
        <polygon points="756,0 1200,0 1200,444 768,444 666,228" fill="url(#panelWork)"/>
      </g>
      <polygon class="accent-yellow" points="800,0 880,0 835,48" fill="var(--yellow)"/>
      <polygon class="accent-yellow" points="666,228 768,444 708,444 660,240" fill="var(--yellow)"/>
      <polygon class="accent-white" points="1125,200 1200,150 1200,320" fill="var(--white)"/>
      <polygon class="accent-yellow" points="1140,262 1200,205 1200,444 1170,444" fill="var(--yellow)"/>
    </svg>

    <div class="brand-mark">
      <span class="brand-mark__dot"></span>
      <span class="brand-mark__name">Dorrish</span>
    </div>

    <h1 class="company-name">DORRISH <span class="company-name__accent">ELECTRIC</span> Ltd</h1>
    <p class="tagline">We do service, custom homes, residential and commercial installations</p>

    <div class="join-button">JOIN US</div>
    <div class="web-address">www.websitename.com</div>
    <div class="social-row">
      <span class="social-row__dot"></span>
      <span class="social-row__dot"></span>
      <span class="social-row__dot"></span>
      <span class="social-row__dot"></span>
      <span class="social-row__handle">/ brandname</span>
    </div>
  </main>
</body>
</html>
```